Looking for a modern, Professional business card design

We have a simple business card, but are looking for a more modern, professional look. A sample of the basic card is attached as well as the logo. We would also like to add that we offer:
Struggling with your finances?
- Learn to become debt free
- Discover the power of cash
- Control your money instead of it controlling you
Let us help you achieve a new level of financial freedom!
Also, we would like to have a "SPECIAL OFFER!: FREE 30 minute consultation"
Financial Planning

```html
<!DOCTYPE html>
<html lang="en">
<head>
<meta charset="utf-8">
<title>ClearPath Money Coaching – Business Card</title>
<link href="https://fonts.googleapis.com/css2?family=Tenor+Sans&family=Roboto+Condensed:wght@300;400&display=swap" rel="stylesheet">
<style>
  :root {
    --card-bg: #1b2d2c;
    --accent: #36e000;
    --ink: #040807;
    --ink-soft: #060b0a;
  }
  html, body {
    margin: 0;
    padding: 0;
    width: 1200px;
    height: 700px;
    overflow: hidden;
    background: var(--card-bg);
  }
  .card {
    position: relative;
    width: 1200px;
    height: 700px;
    background: var(--card-bg);
    font-family: "Tenor Sans", sans-serif;
    overflow: hidden;
  }
  .brand {
    position: absolute;
    left: 48px;
    top: 78px;
    display: flex;
    align-items: center;
    gap: 18px;
  }
  .brand-dot {
    width: 56px;
    height: 56px;
    border-radius: 50%;
    background: var(--accent);
  }
  .brand-name {
    font-family: "Tenor Sans", sans-serif;
    font-size: 34px;
    color: var(--accent);
    letter-spacing: 1px;
  }
  .person-name {
    position: absolute;
    left: 73px;
    top: 268px;
    margin: 0;
    font-weight: 400;
    font-size: 44px;
    letter-spacing: 1.5px;
    color: var(--accent);
  }
  .person-title {
    position: absolute;
    left: 75px;
    top: 332px;
    margin: 0;
    font-size: 23px;
    letter-spacing: 2px;
    color: var(--ink);
  }
  .contact-list {
    position: absolute;
    left: 76px;
    top: 398px;
    margin: 0;
    padding: 0;
    list-style: none;
    font-family: "Roboto Condensed", sans-serif;
    color: var(--ink-soft);
  }
  .contact-item {
    display: flex;
    align-items: center;
    height: 50px;
    margin-bottom: 17px;
  }
  .contact-icon {
    width: 50px;
    height: 50px;
    margin-right: 36px;
    flex: none;
  }
  .contact-phone { font-size: 28px; font-weight: 400; letter-spacing: 1px; }
  .contact-text { font-size: 21px; font-weight: 400; }
  .pitch {
    position: absolute;
    left: 575px;
    top: 228px;
    width: 600px;
    text-align: center;
  }
  .pitch-heading {
    margin: 0 0 62px;
    font-weight: 400;
    font-size: 33px;
    letter-spacing: 2px;
    color: var(--accent);
    white-space: nowrap;
  }
  .pitch-line {
    margin: 0 0 40px;
    font-size: 19px;
    letter-spacing: 1px;
    color: var(--ink);
    line-height: 25px;
    white-space: nowrap;
  }
  .offer-band {
    position: absolute;
    left: 0;
    top: 0;
    width: 1200px;
    height: 700px;
  }
  .offer-text {
    position: absolute;
    right: 18px;
    top: 650px;
    margin: 0;
    font-size: 26px;
    color: var(--ink);
    letter-spacing: 0;
    white-space: nowrap;
  }
  .offer-text small {
    font-size: 20px;
    letter-spacing: 0.8px;
  }
</style>
</head>
<body>
<div class="card">
  <div class="brand">
    <span class="brand-dot"></span>
    <span class="brand-name">ClearPath Money Coaching</span>
  </div>

  <h1 class="person-name">Daniel R. Hayes</h1>
  <p class="person-title">President</p>

  <ul class="contact-list">
    <li class="contact-item">
      <svg class="contact-icon" viewBox="0 0 50 50" fill="none" stroke="#040807" stroke-width="2.4" stroke-linecap="round" stroke-linejoin="round">
        <path d="M10 6 L17 5 L22 16 L17 20 C20 27 24 31 30 34 L34 29 L45 34 L44 41 C42 45 37 46 33 45 C20 41 9 30 5 17 C4 12 6 8 10 6 Z"/>
        <path d="M29 5 C37 6 43 12 45 20"/>
        <path d="M28 12 C33 13 37 16 38 21"/>
      </svg>
      <span class="contact-phone">(205) 555-0182</span>
    </li>
    <li class="contact-item">
      <svg class="contact-icon" viewBox="0 0 50 50" fill="none" stroke="#040807" stroke-width="2.6" stroke-linejoin="round">
        <rect x="4" y="9" width="42" height="32" rx="3"/>
        <path d="M4 11 L25 29 L46 11"/>
        <path d="M4 39 L19 24 M46 39 L31 24"/>
      </svg>
      <span class="contact-text">daniel@clearpathmoneycoach.com</span>
    </li>
    <li class="contact-item">
      <svg class="contact-icon" viewBox="0 0 50 50" fill="none" stroke="#040807" stroke-width="2">
        <circle cx="25" cy="25" r="21"/>
        <ellipse cx="25" cy="25" rx="9" ry="21"/>
        <path d="M4 25 H46 M7 14 H43 M7 36 H43 M25 4 V46"/>
      </svg>
      <span class="contact-text">http://www.clearpathmoneycoach.com</span>
    </li>
  </ul>

  <section class="pitch">
    <h2 class="pitch-heading">Struggling with your finances?</h2>
    <p class="pitch-line">Learn to become debt free</p>
    <p class="pitch-line">Discover the power of cash</p>
    <p class="pitch-line">Control your money instead of it controlling you</p>
    <p class="pitch-line">Let us help you achieve a new level of financial freedom!</p>
  </section>

  <svg class="offer-band" viewBox="0 0 1200 700" aria-hidden="true">
    <path d="M0 651 H545 C560 632 585 618 625 618 H1200 V700 H0 Z" fill="#36e000"/>
  </svg>
  <p class="offer-text">SPECIAL OFFER!: FREE 30 <small>minute consultation</small></p>
</div>
</body>
</html>
```